Larchfield Medical Rooms - Websit, online payment facility and patient information portal

We are a small specialist medical centre inNewcastle NSW, Australia. We would like a modern, open easy to navigate (we have many elderly clients) webpage for our customers to use. We would like a page for content uploads (like referrals etc), an enquiry page, and some patient information pages.

Our logo is attached. We would like a modern, grey scale or black and white website for our customers to use. The landing page should have high resolution images and use san serif font.

Target Market(s)

General Audience, Modern

Industry/Entity Type

Health And Wellness

Coding

Coded - Design and coding required

Number of Pages Required

5+ page

Font styles to use
Sans Serif

Colors
cbcbcb
757575
7f7f7f
c4c4c4
85cae6
cee9f5
cfdfed

Requirements
Must have
• Landing Page
• Several Other pages for content upload
• Ability to do online payments
• Enquiry form
• Contact page
• Social Media Links

```html
<!DOCTYPE html>
<html lang="en">
<head>
<meta charset="utf-8">
<title>Larchfield Medical Rooms</title>
<link rel="stylesheet" href="https://fonts.googleapis.com/css2?family=Raleway:wght@300;400;600;700&display=swap">
<style>
:root{
  --sky:#85cae6;--sky-dark:#4aa6d6;--btn:#3a9ad3;--ink:#222;--grey:#757575;--muted:#9a9a9a;
  --light:#f7f7f7;--line:#e6e6e6;--orange:#f26a1b;--navy:#2a5d8a;--foot:#3d4043;--foot-bar:#323437;
}
*{box-sizing:border-box;margin:0;padding:0}
html,body{width:1200px;height:1200px;overflow:hidden;background:#fff;font-family:'Raleway',sans-serif;color:var(--ink)}
.stage{position:absolute;left:0;top:0;width:1500px;height:1500px;transform:scale(.8);transform-origin:0 0}
.abs{position:absolute}
.page{position:absolute;left:449px;top:0;width:602px;height:1500px;background:#fff}
/* header */
.burger{left:38px;top:25px;width:12px}
.burger i{display:block;height:1.5px;background:#333;margin-bottom:2.5px}
.brand{left:80px;top:5px;width:82px;text-align:center}
.brand .mark{width:14px;height:14px;border-radius:50%;background:#333;margin:0 auto 4px}
.brand b{display:block;font-weight:400;font-size:11px;letter-spacing:-.2px;color:#222}
.brand small{display:block;font-size:4.5px;letter-spacing:1.6px;color:#333}
.nav{left:353px;top:26px;font-size:5px;font-weight:700;letter-spacing:.3px;display:flex;gap:13px;align-items:center}
.nav .login{border:1px solid var(--btn);color:var(--btn);padding:3px 5px}
/* hero */
.hero-side{left:0;top:57px;width:191px;height:226px;background:var(--sky)}
.hero-side ul{list-style:none;position:absolute;left:0;top:40px;width:100%}
.hero-side li{font-size:7px;color:#eaf6fb;padding-left:38px;height:22.6px;line-height:9px}
.hero-side li.active span{display:inline-block;background:var(--sky-dark);color:#fff;margin-left:-38px;padding:1px 8px 1px 38px}
.social-row{position:absolute;left:37px;top:188px;display:flex;gap:18px}
.dot{width:10px;height:10px;border-radius:50%;background:#fff;opacity:.85}
.hero-photo{left:191px;top:57px;width:411px;height:226px;background:linear-gradient(90deg,#eef4f8 0%,#dfe9f0 45%,#f4f6f8 70%,#e4ebf1 100%)}
.hero-copy{left:197px;top:98px;width:175px}
.hero-copy h2{font-size:7.5px;font-weight:700;letter-spacing:.5px;line-height:11px}
.hero-copy p{font-size:5px;color:#555;line-height:9px;margin-top:8px}
.btn-outline{display:inline-block;border:1px solid var(--btn);color:var(--btn);font-size:4.5px;font-weight:700;padding:3px 6px;margin-top:7px;letter-spacing:.3px}
/* newsletter */
.news-title{left:91px;top:315px;width:205px;font-size:20px;font-weight:300;color:#888;line-height:24px;letter-spacing:-.3px;white-space:nowrap}
.news-title b{font-weight:600;color:#222}
.news-note{left:307px;top:319px;width:190px;font-size:5px;color:#999;line-height:8px}
.news-input{left:307px;top:350px;width:125px;height:12px;background:#f1f1f1;font-size:4.5px;color:#aaa;font-style:italic;padding:3px 6px}
.news-btn{left:436px;top:350px;width:50px;height:12px;background:var(--btn);color:#fff;font-size:4.5px;font-weight:700;text-align:center;line-height:12px}
.sep{left:0;top:375px;width:602px;height:1px;background:var(--line)}
/* service circles */
.svc{top:398px;width:124px;height:124px;border:3px solid var(--sky);border-radius:50%;text-align:center;background:#fff}
.svc.focus{border-radius:50% 50% 0 50%}
.svc svg{margin-top:25px}
.svc h3{font-size:7px;font-weight:400;margin-top:8px}
.svc p{font-size:5.5px;color:#aaa;line-height:9px;margin:7px 16px 0}
.svc a{display:block;font-size:4.5px;color:var(--btn);font-weight:700;letter-spacing:.4px;margin-top:5px}
/* portal */
.portal{left:0;top:562px;width:602px;height:270px;background:var(--light)}
.portal h2{position:absolute;top:31px;width:100%;text-align:center;font-size:13px;font-weight:300;color:#555;letter-spacing:-.2px}
.portal h2 b{font-weight:600;color:#222}
.portal .lead{position:absolute;top:54px;left:170px;width:262px;text-align:center;font-size:5.5px;color:#aaa;line-height:9px}
.tiles{position:absolute;left:31px;top:91px;width:542px;height:108px;display:flex}
.tile{flex:1;position:relative;text-align:center;color:#fff}
.tile h4{position:absolute;top:40px;width:100%;font-size:8px;font-weight:700;line-height:9px;letter-spacing:.2px}
.tile span{position:absolute;left:50%;top:64px;transform:translateX(-50%);background:var(--orange);font-size:4.5px;font-weight:700;padding:2px 5px;border-radius:2px;white-space:nowrap}
.browse{position:absolute;left:277px;top:222px;width:50px;height:12px;border:1px solid #aaa;font-size:4.5px;color:#888;text-align:center;line-height:10px}
/* band */
.band{left:0;top:834px;width:602px;height:207px;background:linear-gradient(90deg,#2f6f6c 0%,#497a78 45%,#6e7478 75%,#5a5e62 100%);color:#fff;text-align:center}
.band h2{position:absolute;top:43px;width:100%;font-size:16px;font-weight:300;opacity:.9}
.band .hl{position:absolute;left:219px;top:65px;width:166px;height:20px;background:#fff;color:#555;font-size:17px;font-weight:300;line-height:20px}
.band .sub{position:absolute;top:86px;width:100%;font-size:9.5px;line-height:15px}
.band .fine{position:absolute;top:126px;left:160px;width:282px;font-size:5px;line-height:7px;opacity:.85}
.band .go{position:absolute;left:247px;top:152px;width:108px;height:17px;background:var(--btn);font-size:6.5px;font-weight:700;line-height:17px}
/* agents */
.agents-map{left:40px;top:1045px;width:522px;height:200px;background:radial-gradient(ellipse at center,#f4f5f6 0%,#fff 70%)}
.agents-title{left:0;top:1075px;width:602px;text-align:center;font-size:12px;color:var(--navy)}
.agents-lead{left:0;top:1097px;width:602px;text-align:center;font-size:6px;color:#999}
.avatar{border-radius:50%;background:linear-gradient(180deg,#dfe6ec,#b9c6d2);border:2px solid #fff;box-shadow:0 1px 3px rgba(0,0,0,.2)}
.arrow{width:20px;height:20px;border-radius:50%;background:var(--btn)}
.agent-name{left:0;top:1229px;width:602px;text-align:center;font-size:7.5px}
.agent-role{left:0;top:1243px;width:602px;text-align:center;font-size:5px;color:#ccc}
.agent-desc{left:0;top:1255px;width:602px;text-align:center;font-size:5.5px;color:#999;line-height:8px}
.agent-social{left:274px;top:1279px;display:flex;gap:6px}
.agent-social i{width:14px;height:14px;border-radius:50%;background:#eee}
/* footer */
.footer{left:0;top:1330px;width:602px;height:138px;background:var(--foot);color:#fff}
.col{position:absolute;top:21px;font-size:5px;line-height:9px}
.col h5{font-size:6.5px;font-weight:700;margin-bottom:6px}
.col h5:after{content:"";display:block;width:22px;height:1.5px;background:#fff;margin-top:3px}
.col p{font-size:4.5px;line-height:6px;color:#ddd}
.field{width:90px;height:15px;border:1px solid #777;border-radius:3px;font-size:4.5px;color:#999;padding:3px 5px;margin-bottom:3px}
.send{width:92px;height:14px;border-radius:7px;background:var(--btn);font-size:4.5px;font-weight:700;text-align:center;line-height:14px;margin-top:4px}
.foot-brand{position:absolute;left:86px;top:98px;font-size:11px;color:#888}
.foot-bar{left:0;top:1468px;width:602px;height:32px;background:var(--foot-bar);color:#bbb;font-size:4.5px}
.foot-bar .copy{position:absolute;left:87px;top:13px}
.foot-bar .follow{position:absolute;left:424px;top:11px;display:flex;gap:3px;align-items:center}
.foot-bar .follow i{width:8px;height:8px;border-radius:50%;background:#ddd}
</style>
</head>
<body>
<div class="stage">
<div class="page">
  <header>
    <div class="abs burger"><i></i><i></i><i></i></div>
    <div class="abs brand"><div class="mark"></div><b>LARCHFIELD</b><small>Medical Rooms</small></div>
    <nav class="abs nav"><span>CAREER</span><span>ENGLISH</span><span>SEARCH</span><span class="login">MEMBER LOGIN</span></nav>
  </header>

  <section>
    <div class="abs hero-side">
      <ul>
        <li>Corporate information</li><li>Offering</li><li>Customers</li>
        <li>Partners and Alliances</li><li>Support</li><li class="active"><span>Contact Us</span></li>
      </ul>
      <div class="social-row"><i class="dot"></i><i class="dot"></i><i class="dot"></i><i class="dot"></i></div>
    </div>
    <div class="abs hero-photo" role="img" aria-label="Photo of a smiling doctor with stethoscope and clipboard, clinic staff in the background"></div>
    <div class="abs hero-copy">
      <h2>EIUSMOD TEMPOR INCIDIDUNT UT<br>LABORE ET DOLORE MAGNA ALIQUA UT.</h2>
      <p>Lorem ipsum dolor sit amet, consectetur adipisicing elit, sed do eiusmod tempor incididunt ut labore et dolore magna aliqua.</p>
      <span class="btn-outline">READ MORE &#9656;</span>
    </div>
  </section>

  <section>
    <div class="abs news-title">Enter your email to<br>Subscribe <b>newsletter</b></div>
    <p class="abs news-note">Sign up for our newsletter and receive new cases as we write them – together with editorials with views and thoughts on the latest updates about the Freemium landscape</p>
    <div class="abs news-input">Enter email address</div>
    <div class="abs news-btn">GET STARTED</div>
    <div class="abs sep"></div>
  </section>

  <section>
    <div class="abs svc" style="left:92px">
      <svg width="30" height="24" viewBox="0 0 30 24" fill="none" stroke="#222" stroke-width="1.3"><path d="M15 22 3 10a6 6 0 0 1 12-6 6 6 0 0 1 12 6z"/><path d="M5 12h6l2-4 3 7 2-3h7"/></svg>
      <h3>Our services</h3><p>Nullam varius eget elit nec accumsan usce auctor</p><a>VIEW MORE</a>
    </div>
    <div class="abs svc focus" style="left:238px">
      <svg width="30" height="24" viewBox="0 0 30 24" fill="none" stroke="#222" stroke-width="1.3"><rect x="2" y="6" width="26" height="16" rx="2"/><path d="M10 6V3h10v3M15 10v8M11 14h8"/></svg>
      <h3>Medical centre</h3><p>Ucibus feugiat. Aliquam lacinia dictum luctus.</p><a>VIEW MORE</a>
    </div>
    <div class="abs" style="left:300px;top:460px;width:65px;height:63px;background:var(--sky);z-index:-1"></div>
    <div class="abs svc" style="left:385px">
      <svg width="30" height="24" viewBox="0 0 30 24" fill="none" stroke="#222" stroke-width="1.3"><rect x="9" y="1" width="12" height="4"/><rect x="7" y="5" width="16" height="18" rx="2"/><path d="M11 12h8M11 16h5"/><circle cx="22" cy="19" r="3"/></svg>
      <h3>Medical store</h3><p>Elit nec accumsan usce auctor ucibus feugiat.</p><a>VIEW MORE</a>
    </div>
  </section>

  <section class="abs portal">
    <h2>Websit, <b>online payment facility</b> and patient information portal</h2>
    <p class="lead">Nullam varius eget elit nec accumsan. Fusce auctor faucibus feugiat. Aliquam lacinia dictum luctus. Donec a rutrum mauris.</p>
    <div class="tiles">
      <div class="tile" role="img" aria-label="Photo of the clinic reception" style="background:linear-gradient(160deg,#5a4a3a,#2e2a27)"><h4>LARCHFIELD<br>MEDICAL</h4><span>Learn more</span></div>
      <div class="tile" role="img" aria-label="Photo of a laptop keyboard" style="background:linear-gradient(160deg,#6b4a36,#2a2726)"><h4>ONLINE<br>PAYMENTS</h4><span>Learn more</span></div>
      <div class="tile" role="img" aria-label="Photo of a treatment room" style="background:linear-gradient(160deg,#3f5468,#22303d)"><h4>MEDICAL<br>ROOMS</h4><span>Learn more</span></div>
      <div class="tile" role="img" aria-label="Photo of payment cards" style="background:linear-gradient(160deg,#8a6a2a,#4a3c26)"><h4>PAYMENT<br>FACILITY</h4><span>Learn more</span></div>
      <div class="tile" role="img" aria-label="Photo of surgeons at work" style="background:linear-gradient(160deg,#4a5f80,#2b3750)"><h4>PATIENT<br>INFORMATION</h4><span>Learn more</span></div>
    </div>
    <div class="browse">BROWSE ALL</div>
  </section>

  <section class="abs band" role="img" aria-label="Background photo of a globe and a stethoscope in teal tones">
    <h2>Lorem Ipsum is simply dummy text</h2>
    <div class="hl">since the 1500s,</div>
    <p class="sub">When an unknown printer took a galley type and<br>scrambled it to specimen book.</p>
    <p class="fine">It has survived not only five centuries, but also the leap into electronic typesetting, remaining essentially unchanged. It was popularised in the 1960s with the release</p>
    <div class="go">START YOUR SEARCH</div>
  </section>

  <section>
    <div class="abs agents-map" role="img" aria-label="Faint world map backdrop"></div>
    <h2 class="abs agents-title">Top Agents at your Service</h2>
    <p class="abs agents-lead">Duis aute irure dolor in reprehenderit in voluptate velit esse cillum dolore eu.</p>
    <div class="abs arrow" style="left:195px;top:1174px"></div>
    <div class="abs avatar" role="img" aria-label="Agent portrait" style="left:218px;top:1160px;width:28px;height:28px"></div>
    <div class="abs avatar" role="img" aria-label="Agent portrait" style="left:244px;top:1150px;width:34px;height:34px"></div>
    <div class="abs avatar" role="img" aria-label="Agent portrait" style="left:271px;top:1137px;width:60px;height:60px"></div>
    <div class="abs avatar" role="img" aria-label="Agent portrait" style="left:326px;top:1150px;width:34px;height:34px"></div>
    <div class="abs avatar" role="img" aria-label="Agent portrait" style="left:360px;top:1160px;width:28px;height:28px"></div>
    <div class="abs arrow" style="left:387px;top:1174px"></div>
    <div class="abs agent-name">Maren Holt</div>
    <div class="abs agent-role">Doctor</div>
    <p class="abs agent-desc">Insurance agent with over 15 years of<br>experience in insurance business.</p>
    <div class="abs agent-social"><i></i><i></i><i></i></div>
  </section>

  <footer>
    <div class="abs footer">
      <div class="col" style="left:84px;width:118px"><h5>About Larchfield Medical Rooms</h5>
        <p>voluptatem accusantium doloremque audantium, totam rem aperiamdoloremque audantium,totam rem aperiaolpub voluptdoloremque.</p><br>
        <p>audantium rem aperiamo,otam rem aperiamolore mque audantium,otam rem aperiamolore....</p></div>
      <div class="col" style="left:218px"><h5>Quick Link</h5>Home<br>About us<br>Dermatoglyphics<br>Beep<br>Research<br>Contacts</div>
      <div class="col" style="left:291px;width:90px"><h5>Contact us</h5>
        <p>&#9679; 1208 Harbour View Lane<br>&nbsp;&nbsp; Newcastle NSW 2300</p>&#9990; 02-5550-1842<br>&#9632; 02-5550-1843<br>&#9993; info@larchfieldrooms.example</div>
      <div class="col" style="left:399px"><h5 style="margin-bottom:4px">Quick contact</h5>
        <div class="field">Name</div><div class="field">Email</div><div class="field" style="height:30px">Message</div><div class="send">SEND NOW</div></div>
      <div class="foot-brand">LARCHFIELD</div>
    </div>
    <div class="abs foot-bar">
      <span class="copy">© 2015 All Rights Reserved, Larchfield Medical Rooms &nbsp;|&nbsp; Privacy and Terms &amp; Conditions</span>
      <span class="follow">Follow us on &nbsp;<i></i><i></i><i></i><i></i></span>
    </div>
  </footer>
</div>
</div>
</body>
</html>
```